Business Card Redesign

We would like to redesign our existing business cards.
The new design shall look:
ELEGANT, LUXURY, PROFESSIONAL
Reference:
YOU CAN VISIT WWW.LUMEN-RIVET.HK FOR BETTER UNDERSTANDING OF COMPANY STRATEGY AND POSITION
Additional:
CHOSEN CANDIDATE SHALL PROVIDE THE INSTRUCTION OF PRINTING IF ANY THERMAL COVERAGE OR ANY ADDITION IS OFFERED
Industry/Entity Type
Business

```html
<!DOCTYPE html>
<html lang="en">
<head>
<meta charset="utf-8">
<title>Lumen Rivet Limited – Business Card</title>
<link rel="stylesheet" href="https://fonts.googleapis.com/css2?family=Source+Sans+3:wght@400;600&display=swap">
<style>
  :root {
    --page: #ffffff;
    --card: #ffffff;
    --band: #6e5434;
    --brown-text: #6b4a2b;
    --band-light: #e6ddd0;
    --band-muted: #d6c8b3;
    --accent-blue: #1e5fa8;
    --body-text: #333333;
    --rule: #9a9a9a;
    --mark-fill: #e9a93a;
    --mark-ring: #1f4f8f;
  }
  html, body {
    margin: 0;
    padding: 0;
    width: 1200px;
    height: 1000px;
    overflow: hidden;
    background: var(--page);
    font-family: "Source Sans 3", "Myriad Pro", Arial, sans-serif;
  }
  .canvas {
    position: relative;
    width: 1200px;
    height: 1000px;
  }
  .business-card {
    position: absolute;
    left: 363px;
    top: 362px;
    width: 482px;
    height: 276px;
    background: var(--card);
    box-shadow: 6px 8px 14px rgba(0,0,0,0.45);
    overflow: hidden;
  }
  .company-name {
    position: absolute;
    left: 179px;
    top: 14px;
    margin: 0;
    font-size: 26px;
    font-weight: 400;
    color: var(--brown-text);
    letter-spacing: 0.2px;
  }
  .identity-band {
    position: absolute;
    left: 0;
    top: 53px;
    width: 100%;
    height: 85px;
    background: var(--band);
  }
  .brand-mark {
    position: absolute;
    left: 40px;
    top: 39px;
    width: 114px;
    height: 114px;
    border-radius: 50%;
    background: var(--mark-fill);
    border: 4px solid var(--mark-ring);
    box-sizing: border-box;
    display: flex;
    align-items: center;
    justify-content: center;
    text-align: center;
    font-size: 15px;
    font-weight: 600;
    line-height: 1.1;
    color: var(--mark-ring);
  }
  .person-name {
    position: absolute;
    left: 181px;
    top: 66px;
    margin: 0;
    font-size: 20px;
    font-weight: 400;
    color: #ffffff;
  }
  .person-role {
    position: absolute;
    left: 181px;
    top: 92px;
    margin: 0;
    font-size: 12px;
    color: var(--band-muted);
  }
  .direct-contact {
    position: absolute;
    right: 25px;
    top: 103px;
    margin: 0;
    text-align: right;
    font-size: 12.5px;
    line-height: 14px;
    color: var(--band-light);
  }
  .office-label {
    position: absolute;
    left: 80px;
    top: 177px;
    margin: 0;
    font-size: 12.5px;
    color: var(--accent-blue);
  }
  .office-address {
    position: absolute;
    left: 79px;
    top: 199px;
    margin: 0;
    font-style: normal;
    font-size: 12.5px;
    line-height: 12.5px;
    color: var(--body-text);
  }
  .office-divider {
    position: absolute;
    left: 264px;
    top: 204px;
    width: 1px;
    height: 35px;
    background: var(--rule);
  }
  .office-lines {
    position: absolute;
    left: 277px;
    top: 200px;
    margin: 0;
    font-size: 12.5px;
    line-height: 13.5px;
    color: var(--body-text);
  }
  .website {
    position: absolute;
    top: 239px;
    margin: 0;
    font-size: 12.5px;
    font-weight: 600;
    color: var(--accent-blue);
  }
  .website-start { left: 79px; }
  .website-end { left: 170px; }
</style>
</head>
<body>
<main class="canvas">
  <article class="business-card">
    <h1 class="company-name">Lumen Rivet Limited</h1>
    <div class="identity-band"></div>
    <div class="brand-mark">Lumen<br>Rivet</div>
    <h2 class="person-name">Nora Vell</h2>
    <p class="person-role">PR Consultant</p>
    <p class="direct-contact">nora@lumen-rivet.hk<br>(852) 6140 3827</p>

    <p class="office-label">Headquarters (Hong Kong)</p>
    <address class="office-address">Rm. 1204B, 12/F, Harbourline,<br>58 Aberdeen Street, Central,<br>Hong Kong</address>
    <div class="office-divider"></div>
    <p class="office-lines">Tel: (852) 2930-4418<br>Fax: (852) 2930-4419</p>
    <p class="website website-start">www.lumen-</p>
    <p class="website website-end">rivet.hk</p>
  </article>
</main>
</body>
</html>
```